Cobra Vane Systems Website Revamp

We need a full website for the oil and gas sector to showcase our company and our technology/services we provide to larger corporations. We want our website represent innovation and identity.

Background:

We are a service based company that specializes in:

- well services, and
-permanent applications
**(Please be aware that these are two different aspects to the oil and gas sector, both of which we supply to our customers)

We provide a wide range of jet pump technologies to address under performing reservoirs or problematic well producing conditions. We have field operations currently in: Canada, Oman, and Australia with efforts currently underway to expand in other markets. Therefore are needing a website to help promote a better comprehension of what we do and how we can solve their well issues. We are looking for

1.) Identity;
2.) Emphasis on better comprehension of our services for our clients to relate to us as a solution to their needs;
3.) User friendly interface - but new and exciting in this digital age .

Some examples of websites we like:

http://brindlowinc.com/how-we-work/
http://www.qorvantix.com/qorvan-system/
https://velmorafield.com/

Videos of our technologies:

https://www.clipvarro.com/watch?v=519KdpQWzRe
https://www.clipvarro.com/watch?v=t7NBwuhsp43

Target Market(s)

Petroleum Industry Clients

Coding

Coded - Design and coding required

Number of Pages Required

5+ page

Colors

Designer to choose colors to be used in the design.

Requirements
Must have
• See Project Description, and feel free to contact us with any questions/inquiries!
Nice to have
• Our color scheme is generally 'blue', to depict jet pumps (our service). However, we are open to ideas and artistic interpretation. Grayscale/offset colors/highlight colors etc.

```html
<!DOCTYPE html>
<html lang="en">
<head>
<meta charset="utf-8">
<title>Cobra Vane Systems</title>
<link rel="stylesheet" href="https://fonts.googleapis.com/css2?family=Josefin+Sans:wght@400;600;700&family=EB+Garamond:wght@400;600&display=swap">
<style>
:root{
  --navy:#1f3c58;
  --steel:#2d5f8c;
  --steel-dark:#0f2a47;
  --ice:#9fc6e6;
  --text-body:#5a5f66;
  --gray-challenge:#b6b7b9;
  --gray-apps:#d6d8dc;
  --icon-tile:#b9bdc1;
  --gray-solution:#e4e4e4;
  --footer:#1e1e1e;
  --white:#ffffff;
}
*{margin:0;padding:0;box-sizing:border-box}
html,body{width:1200px;height:2462px;overflow:hidden}
body{position:relative;background:var(--white);font-family:"EB Garamond",Georgia,serif}
.abs{position:absolute}
h1,h2,h3,h4{font-weight:400}

/* hero */
.hero{left:0;top:0;width:1200px;height:698px;
  background:
    radial-gradient(ellipse 520px 240px at 62% 34%,rgba(190,225,245,.55) 0%,rgba(190,225,245,0) 70%),
    radial-gradient(ellipse 380px 300px at 18% 42%,rgba(150,200,235,.45) 0%,rgba(150,200,235,0) 70%),
    radial-gradient(ellipse 420px 200px at 88% 60%,rgba(170,210,240,.4) 0%,rgba(170,210,240,0) 70%),
    linear-gradient(170deg,#2a5680 0%,#4d80ad 30%,#243f66 55%,#30588a 75%,#0d1f38 100%)}
.hero-shade{left:0;top:0;width:1200px;height:698px;
  background:linear-gradient(180deg,rgba(10,25,45,.35),rgba(10,25,45,0) 35%,rgba(10,25,45,0) 70%,rgba(10,25,45,.5))}
.nav-band{left:0;top:32px;width:1200px;height:95px;
  background:linear-gradient(180deg,rgba(20,55,90,.8),rgba(12,36,64,.85));
  border-bottom:2px solid rgba(170,205,235,.55)}
.nav-item{top:60px;font-family:"Josefin Sans",sans-serif;color:var(--white);text-align:right}
.nav-item small{display:block;font-size:14px;line-height:15px;text-transform:lowercase}
.nav-item span{display:block;font-size:20.5px;line-height:24px;letter-spacing:.4px}
.hero-title{left:616px;top:410px;font-family:"Josefin Sans",sans-serif;font-size:45px;color:var(--white);letter-spacing:.5px;text-shadow:0 2px 8px rgba(0,20,40,.45)}
.hero-sub{left:617px;top:460px;font-family:"Josefin Sans",sans-serif;font-size:12.5px;color:#c9dcec;letter-spacing:1px;text-shadow:0 1px 3px rgba(0,20,40,.6)}
.strip{left:0;width:1200px;background:linear-gradient(180deg,#4c7fae,#1c446e)}

/* challenges */
.challenges{left:0;top:711px;width:1200px;height:558px;
  background:radial-gradient(ellipse at 20% 40%,#c9cacc 0%,var(--gray-challenge) 70%)}
.section-title{font-family:"Josefin Sans",sans-serif;color:var(--navy)}
.challenge-heading{font-family:"Josefin Sans",sans-serif;font-size:23px;color:var(--navy);letter-spacing:.5px}
.challenge-body{font-size:18.5px;line-height:29px;color:var(--text-body);width:455px}
.card-frame{left:639px;top:790px;width:456px;height:458px;background:#cfd0d2}
.card{left:668px;width:397px;height:118px;background:var(--white);box-shadow:0 4px 6px rgba(0,0,0,.2)}

/* apps */
.apps{left:0;top:1269px;width:1200px;height:378px;background:var(--gray-apps)}
.apps-title{left:0;top:1342px;width:1200px;text-align:center;font-family:"Josefin Sans",sans-serif;font-size:24px;font-weight:600;letter-spacing:3.5px;color:#3a3a3a}
.icon-tile{top:1418px;width:148px;height:148px;border-radius:14px;background:var(--icon-tile)}

/* solutions */
.solutions{left:0;top:1663px;width:1200px;height:471px;background:var(--gray-solution)}
.solutions-title{left:52px;top:1728px;font-family:"Josefin Sans",sans-serif;font-size:39px;color:#4e5e6c;letter-spacing:1.5px}
.solutions-quote{left:52px;top:1797px;width:380px;font-size:22.5px;line-height:44.5px;color:#3b3b3b}
.learn-more{left:50px;top:2004px;font-family:"Josefin Sans",sans-serif;font-size:24px;color:#2d3a48;letter-spacing:1px}
.solutions-photo{left:514px;top:1717px;width:609px;height:333px;
  background:linear-gradient(120deg,#e58a3a 0%,#d9a070 30%,#6f8fb0 55%,#2b3d55 100%);
  border:2px solid #c9c9c9;box-shadow:0 3px 8px rgba(0,0,0,.25)}

/* footer */
.footer{left:0;top:2216px;width:1200px;height:246px;background:var(--footer)}
.footer-heading{top:2256px;font-family:"Josefin Sans",sans-serif;font-size:17px;font-weight:700;color:var(--white);letter-spacing:.5px}
.footer-text{font-size:15.5px;font-weight:600;line-height:23px;color:var(--white)}
.footer-link{font-family:"Josefin Sans",sans-serif;font-size:11.5px;font-weight:700;color:var(--white)}
.footer-list{list-style:none;font-size:15px;font-weight:600;line-height:23px;color:var(--white);text-transform:uppercase}
</style>
</head>
<body>

<!-- hero -->
<div class="abs hero" role="img" aria-label="Industrial plant interior with large steel pipes in blue light"></div>
<div class="abs hero-shade"></div>
<div class="abs nav-band"></div>
<nav>
  <div class="abs nav-item" style="left:451px"><small>technologies</small><span>WHAT WE DO</span></div>
  <div class="abs nav-item" style="left:645px"><small>about us</small><span>WHO WE ARE</span></div>
  <div class="abs nav-item" style="left:832px"><small>services</small><span>PRODUCTS</span></div>
  <div class="abs nav-item" style="left:995px"><small>&nbsp;</small><span>CONTACT US</span></div>
</nav>
<h1 class="abs hero-title">LOREM IPSUM</h1>
<p class="abs hero-sub">PHARETRA FAUCIBUS AD QUOQUE</p>
<div class="abs strip" style="top:698px;height:13px"></div>

<!-- challenges -->
<section class="abs challenges"></section>
<h2 class="abs section-title" style="left:54px;top:750px;font-size:30px">Challenges</h2>
<h3 class="abs challenge-heading" style="left:50px;top:832px">PRODUCTION SYSTEMS PROBLEMS</h3>
<p class="abs challenge-body" style="left:50px;top:880px">Sed in dui in augue consectetur lobortis. Pellentesque orci tellus, imperdiet interdum nibh a, varius gravida augue. Curabitur faucibus, lectus vitae maximus</p>
<h3 class="abs challenge-heading" style="left:50px;top:1023px">QUOD QUANTUM</h3>
<p class="abs challenge-body" style="left:50px;top:1071px">Lorem ipsum dolor sit amet, consectetur adipiscing elit. Praesent hendrerit quis enim ac vehicula. Sed in dui in augue consectetur lobortis. Pellentesque orci tellus, imperdiet interdum nibh a, varius gravida augue. Curabitur faucibus, lectus vitae maximus</p>

<div class="abs card-frame"></div>
<div class="abs card" style="top:814px" role="img" aria-label="Green industrial skyline illustration"><div style="margin:30px 14px 12px;height:62px;background:linear-gradient(180deg,#9fd86a,#4caf2f)"></div></div>
<div class="abs card" style="top:957px" role="img" aria-label="Orange and red industrial skyline illustration"><div style="margin:30px 14px 12px;height:62px;background:linear-gradient(180deg,#f6b23c,#e0401e)"></div></div>
<div class="abs card" style="top:1098px" role="img" aria-label="Teal industrial skyline illustration"><div style="margin:30px 14px 12px;height:62px;background:linear-gradient(180deg,#8fd6de,#1e9aaa)"></div></div>

<!-- apps -->
<section class="abs apps"></section>
<h2 class="abs apps-title">APPS / ICONS</h2>
<div class="abs icon-tile" style="left:110px"></div>
<div class="abs icon-tile" style="left:359px"></div>
<div class="abs icon-tile" style="left:612px"></div>
<div class="abs icon-tile" style="left:854px"></div>
<div class="abs strip" style="top:1647px;height:16px"></div>

<!-- solutions -->
<section class="abs solutions"></section>
<svg class="abs" style="left:0;top:1663px" width="1200" height="471" viewBox="0 0 1200 471">
  <path d="M0 30 C300 70 700 10 1200 40 L1200 0 L0 0Z" fill="#cfd1d3"/>
  <path d="M0 60 C400 110 800 30 1200 70" stroke="#f2f2f2" stroke-width="3" fill="none"/>
</svg>
<h2 class="abs solutions-title">SOLUTIONS</h2>
<p class="abs solutions-quote">“et sistema quod maxit perdurescet durabilis infra quod magis eternatitem magistima chose perception randa quod vivendum”</p>
<a class="abs learn-more">LEARN MORE</a>
<div class="abs solutions-photo" role="img" aria-label="Factory worker in orange shirt and overalls in a machine workshop"></div>

<!-- footer -->
<svg class="abs" style="left:0;top:2134px" width="1200" height="82" viewBox="0 0 1200 82">
  <defs><linearGradient id="footerBand" x1="0" y1="0" x2="0" y2="1">
    <stop offset="0" stop-color="#c9cbce"/><stop offset="1" stop-color="#5d6166"/></linearGradient></defs>
  <rect width="1200" height="82" fill="url(#footerBand)"/>
  <path d="M0 82 L310 82 C370 82 380 44 440 44 L1200 44 L1200 82Z" fill="var(--footer)"/>
</svg>
<footer class="abs footer"></footer>
<h4 class="abs footer-heading" style="left:51px">OUR LOCATION</h4>
<p class="abs footer-text" style="left:51px;top:2310px;width:195px;line-height:35px">Lipsum quoque 10, et per 23, perque, Et sit</p>
<a class="abs footer-link" style="left:53px;top:2408px">SEE ON MAPS</a>
<h4 class="abs footer-heading" style="left:424px">LINKS</h4>
<ul class="abs footer-list" style="left:422px;top:2302px"><li>Home</li><li>Portfolio</li><li>Services</li><li>About</li><li>Contact</li></ul>
<h4 class="abs footer-heading" style="left:607px">ABOUT US</h4>
<p class="abs footer-text" style="left:605px;top:2302px;width:215px">&nbsp;Suspendisse aliquet purus et lectus consequat, vel auctor ante auctor. Nam et sapien</p>
<a class="abs footer-link" style="left:609px;top:2408px">READ MORE</a>
<h4 class="abs footer-heading" style="left:973px">COMPANY</h4>
<ul class="abs footer-list" style="left:972px;top:2302px"><li>Pharetra</li><li>Ecit</li><li>Perque</li><li>Ed sae</li><li>Quoque</li></ul>

</body>
</html>
```